Pediatric Dentist Business Card

I need a business card designed for a dentist who works exclusively with children.
We prefer designs that are out of ordiary that is fun and interesting to kids.

there is no logo since this is a dentists office. The name of the doctor is "Tavor Kesh" if you want to get creative with that.

Target Market(s)

Kids

Industry/Entity Type

Business

Contact Information for Business Card

Anythings that is creative

Colors

Designer to choose colors to be used in the design.

```html
<!DOCTYPE html>
<html lang="en">
<head>
<meta charset="utf-8">
<title>Tavor Kesh – Pediatric Dentist Business Card</title>
<link href="https://fonts.googleapis.com/css2?family=Questrial&display=swap" rel="stylesheet">
<style>
  :root {
    --backdrop: #646464;
    --card: #ffffff;
    --ink: #111111;
    --sky: #00adee;
    --magenta: #ec008c;
    --lime: #a5bf3c;
    --brand-red: #ed1c24;
    --on-band: #ffffff;
  }
  * { box-sizing: border-box; margin: 0; padding: 0; }
  html, body {
    width: 1185px;
    height: 1200px;
    overflow: hidden;
    background: var(--backdrop);
    font-family: "Questrial", "Century Gothic", sans-serif;
  }
  .canvas { position: relative; width: 1185px; height: 1200px; }
  .card {
    position: absolute;
    left: 248px;
    width: 690px;
    height: 386px;
    background: var(--card);
    overflow: hidden;
  }
  .card--front { top: 190px; }
  .card--back { top: 623px; }

  .brand {
    position: absolute;
    inset: 0;
    display: flex;
    align-items: center;
    justify-content: center;
    gap: 22px;
  }
  .brand__dot {
    width: 64px;
    height: 64px;
    border-radius: 50%;
    background: var(--brand-red);
  }
  .brand__name {
    font-size: 54px;
    font-weight: 400;
    color: var(--brand-red);
    letter-spacing: 0.5px;
  }

  .holder-name {
    position: absolute;
    top: 0;
    left: 0;
    width: 100%;
    height: 202px;
    display: flex;
    align-items: center;
    justify-content: center;
    padding-top: 22px;
    font-size: 46px;
    font-weight: 400;
    color: var(--ink);
    letter-spacing: 0.5px;
  }
  .contact-row {
    position: absolute;
    left: 0;
    bottom: 0;
    width: 100%;
    height: 184px;
    display: flex;
  }
  .contact {
    flex: 1;
    display: flex;
    flex-direction: column;
    align-items: center;
    color: var(--on-band);
    font-size: 19px;
  }
  .contact--address { background: var(--sky); }
  .contact--email { background: var(--magenta); }
  .contact--phone { background: var(--lime); }
  .contact__icon { margin-top: 26px; height: 58px; display: flex; align-items: center; }
  .contact__text { margin-top: 14px; white-space: nowrap; }
</style>
</head>
<body>
<main class="canvas">
  <section class="card card--front">
    <div class="brand">
      <span class="brand__dot" aria-hidden="true"></span>
      <span class="brand__name">Tavor Kesh</span>
    </div>
  </section>

  <section class="card card--back">
    <h1 class="holder-name">Tavor Kesh</h1>
    <div class="contact-row">
      <div class="contact contact--address">
        <span class="contact__icon">
          <svg width="56" height="52" viewBox="0 0 56 52" aria-hidden="true">
            <polyline points="3,26 28,4 53,26" fill="none" stroke="#fff" stroke-width="6" stroke-linejoin="round"/>
            <path d="M11 26 L28 12 L45 26 V52 H33 V38 H23 V52 H11 Z" fill="#fff"/>
          </svg>
        </span>
        <span class="contact__text">45 Elm Way</span>
      </div>
      <div class="contact contact--email">
        <span class="contact__icon">
          <svg width="56" height="38" viewBox="0 0 56 38" aria-hidden="true">
            <rect x="0" y="0" width="56" height="38" fill="#fff"/>
            <polyline points="3,3 28,22 53,3" fill="none" stroke="#ec008c" stroke-width="3"/>
            <polyline points="3,35 21,17" fill="none" stroke="#ec008c" stroke-width="3"/>
            <polyline points="53,35 35,17" fill="none" stroke="#ec008c" stroke-width="3"/>
          </svg>
        </span>
        <span class="contact__text">abc@kidmail.com</span>
      </div>
      <div class="contact contact--phone">
        <span class="contact__icon">
          <svg width="44" height="50" viewBox="0 0 24 24" aria-hidden="true">
            <path fill="#fff" d="M6.6 10.8c1.4 2.8 3.8 5.1 6.6 6.6l2.2-2.2c.3-.3.7-.4 1-.2 1.1.4 2.3.6 3.6.6.6 0 1 .4 1 1V20c0 .6-.4 1-1 1C10.6 21 3 13.4 3 4c0-.6.4-1 1-1h3.5c.6 0 1 .4 1 1 0 1.3.2 2.5.6 3.6.1.3 0 .7-.2 1z" transform="rotate(-10 12 12)"/>
          </svg>
        </span>
        <span class="contact__text">555 0142 987</span>
      </div>
    </div>
  </section>
</main>
</body>
</html>
```